Business Card Design Project

I am seeking a business card for my life coaching career. I specialize in coaching executives and entrepreneurs. Consciousness plays a key role in my practice.
Updates

I would like to see different fonts -I don't like the way the capital J looks. I only want my name once on the card, on the front. I like everything centered on the front, with a white background, grey and green on the front; and the same grey on the back with bullet points next to each quality; centered. I like a subtle shadow of the mountains behind the text on the back of the card. I don't want the mountains on either side to be too big. Thank you.

Target Market(s)

Middle age business owners/executives

Industry/Entity Type

Business

Contact Information for Business Card

The front design is my name and a mountain logo. I want to have my name prominently shown.

Requirements
Must have
• Front of card:
• My name prominent sized font
• Helping clients lead more fulfilling lives;
• Executive Life Coach
• 555-304-7781
• rkovet4@mailbriar.com
• Back of Card:
• Providing Unparalleled support
• Providing a safe place to grow in self-awareness
• 20+ years entrepreneurial experience
• Trust
• Integrity
Nice to have
• Easy to read font; warm colors reflecting a masculine personality.

Files

```html
<!DOCTYPE html>
<html lang="en">
<head>
<meta charset="utf-8">
<title>Rowan Kovet — Business Card</title>
<link rel="stylesheet" href="https://fonts.googleapis.com/css2?family=Lato:wght@400;700;900&display=swap">
<style>
  :root {
    --bg: #2b2b2b;
    --card: #f4f4f4;
    --card-edge: #e2e2e2;
    --green: #4f6b34;
    --grey: #555555;
    --grey-strip: #4a4a4a;
    --text: #3d3d3d;
    --band-text: #e9eee3;
  }
  * { margin: 0; padding: 0; box-sizing: border-box; }
  html, body { width: 1200px; height: 997px; overflow: hidden; }
  body {
    background: var(--bg);
    font-family: "Lato", Arial, sans-serif;
    position: relative;
  }
  .card {
    position: absolute;
    width: 580px;
    height: 332px;
    border-radius: 18px;
    background: linear-gradient(180deg, #ffffff 0%, var(--card) 60%, var(--card-edge) 100%);
    overflow: hidden;
    box-shadow: 0 18px 40px rgba(0,0,0,0.55);
  }
  .card-back { left: 70px; top: 80px; }
  .card-front { left: 550px; top: 500px; }

  /* back */
  .values-band {
    height: 58px;
    background: var(--green);
    color: var(--band-text);
    display: flex;
    align-items: center;
    justify-content: center;
    gap: 22px;
    font-size: 20px;
    letter-spacing: 6px;
  }
  .values-divider { width: 2px; height: 26px; background: var(--band-text); }
  .back-body {
    height: 274px;
    display: flex;
    flex-direction: column;
    align-items: center;
    justify-content: center;
    text-align: center;
  }
  .back-tagline {
    color: var(--green);
    font-weight: 700;
    font-size: 16px;
    letter-spacing: 1.5px;
  }
  .qualities { margin-top: 22px; list-style: none; }
  .qualities li {
    color: var(--grey);
    font-size: 17px;
    letter-spacing: 0.5px;
    text-transform: uppercase;
    line-height: 1.6;
  }
  .qualities li::before {
    content: "\2022";
    color: var(--green);
    margin-right: 8px;
  }

  /* front */
  .front-brand { text-align: center; padding-top: 38px; }
  .brand-name {
    color: var(--green);
    font-weight: 900;
    font-size: 46px;
    line-height: 1;
  }
  .brand-tagline {
    color: var(--green);
    font-weight: 700;
    font-size: 13px;
    letter-spacing: 1.5px;
    margin-top: 6px;
  }
  .front-details {
    display: flex;
    align-items: center;
    justify-content: center;
    margin-top: 28px;
    gap: 34px;
  }
  .holder-title {
    color: var(--grey);
    font-weight: 700;
    font-size: 20px;
  }
  .details-divider { width: 3px; height: 82px; background: var(--green); border-radius: 2px; }
  .contacts { list-style: none; }
  .contacts li {
    display: flex;
    align-items: center;
    gap: 10px;
    color: var(--text);
    font-size: 17px;
    line-height: 1;
    margin: 9px 0;
  }
  .contact-icon { width: 24px; height: 24px; flex: none; }
  .front-strip {
    position: absolute; left: 0; right: 0; bottom: 58px;
    height: 8px; background: var(--grey-strip);
  }
  .front-band {
    position: absolute; left: 0; right: 0; bottom: 0;
    height: 58px; background: var(--green);
  }
</style>
</head>
<body>

  <section class="card card-back" aria-label="Card back">
    <div class="values-band">
      <span>TRUST</span>
      <span class="values-divider"></span>
      <span>INTEGRITY</span>
    </div>
    <div class="back-body">
      <div class="back-tagline">Helping Clients lead more fulfilling lives</div>
      <ul class="qualities">
        <li>Providing unparalleled support</li>
        <li>Providing a safe place to grow in self-awareness</li>
        <li>20+ years entrepreneurial experience</li>
      </ul>
    </div>
  </section>

  <section class="card card-front" aria-label="Card front">
    <div class="front-brand">
      <div class="brand-name">Rowan Kovet</div>
      <div class="brand-tagline">Helping Clients lead more fulfilling lives</div>
    </div>
    <div class="front-details">
      <div class="holder-title">Executive Life Coach</div>
      <span class="details-divider"></span>
      <ul class="contacts">
        <li>
          <svg class="contact-icon" viewBox="0 0 24 24" aria-hidden="true">
            <circle cx="12" cy="12" r="12" fill="#4f6b34"/>
            <path d="M7 9.5c0-1.5 2.2-2.5 5-2.5s5 1 5 2.5v1h-2.4V9.3h-5.2v1.2H7z M8.5 11.5h7l1 5h-9z" fill="#fff"/>
            <circle cx="12" cy="14" r="1.3" fill="#4f6b34"/>
          </svg>
          <span>555-304-7781</span>
        </li>
        <li>
          <svg class="contact-icon" viewBox="0 0 24 24" aria-hidden="true">
            <circle cx="12" cy="12" r="12" fill="#4f6b34"/>
            <rect x="6" y="8" width="12" height="8.5" rx="1" fill="#fff"/>
            <path d="M6.5 8.6 12 13l5.5-4.4" fill="none" stroke="#4f6b34" stroke-width="1.2"/>
          </svg>
          <span>rkovet4@mailbriar.com</span>
        </li>
      </ul>
    </div>
    <div class="front-strip"></div>
    <div class="front-band"></div>
  </section>

</body>
</html>
```